Email Marketing Campaign Templates

Email drip childcare campaign designed to communicate with parents interested in services. We would like the template(s) to be created so that we can change the content as needed.I will add below collateral that we have used in the past as well as logo.
three to for templates 1.) welcome template 2/ things to bring 3) generic template
Target Market(s)
Parents and Millennials
Industry/Entity Type
Childcare
Colors
85cae6
0493ce
9bcb3c
add136
fefefe
faa54b
cadf82
86cae7
33a6d7
Requirements
Must have
- Photos of staff with children
Nice to have
- Photos

```html
<!DOCTYPE html>
<html lang="en">
<head>
<meta charset="utf-8">
<title>Bloomwell Early Learning – Email Templates</title>
<link href="https://fonts.googleapis.com/css2?family=Patrick+Hand&family=Questrial&display=swap" rel="stylesheet">
<style>
  :root {
    --blue: #0493ce;
    --blue-mid: #33a6d7;
    --blue-soft: #85cae6;
    --green: #9bcb3c;
    --green-soft: #cadf82;
    --orange: #faa54b;
    --white: #fefefe;
    --frame: #3a9fd6;
    --heading-font: "Patrick Hand", cursive;
    --body-font: "Questrial", sans-serif;
  }
  * { box-sizing: border-box; margin: 0; padding: 0; }
  html, body { width: 772px; height: 1200px; overflow: hidden; background: var(--white); }
  body { position: relative; font-family: var(--body-font); }

  .email { position: absolute; border: 1px solid var(--frame); background: var(--white); overflow: hidden; }
  .email--welcome { left: 18px; top: 22px; width: 705px; height: 349px; }
  .email--bring   { left: 21px; top: 405px; width: 705px; height: 349px; }
  .email--generic { left: 21px; top: 787px; width: 707px; height: 351px; }

  .intro { position: absolute; left: 0; top: 0; width: 222px; height: 100%; text-align: center; }
  .brand { position: absolute; left: 0; top: 92px; width: 100%; display: flex; align-items: center; justify-content: center; gap: 7px; }
  .brand__dot { width: 14px; height: 14px; border-radius: 50%; background: var(--green); }
  .brand__name { font-family: var(--body-font); font-size: 17px; color: var(--blue-mid); line-height: 1.1; text-align: left; }
  .intro__title { position: absolute; left: 0; width: 100%; font-family: var(--heading-font); font-weight: 400; color: var(--green); font-size: 40px; line-height: 0.78; letter-spacing: 1.5px; }
  .intro__text { position: absolute; left: 20px; width: 188px; text-align: left; font-size: 15px; line-height: 1.3; color: var(--blue); }

  .pattern-strip { position: absolute; top: 0; height: 100%; }
  .pattern-strip--blue {
    background:
      radial-gradient(circle at 30% 12%, rgba(255,255,255,.22) 0 9px, transparent 10px),
      radial-gradient(circle at 70% 38%, rgba(255,255,255,.18) 0 11px, transparent 12px),
      radial-gradient(circle at 35% 64%, rgba(255,255,255,.2) 0 10px, transparent 11px),
      radial-gradient(circle at 68% 88%, rgba(255,255,255,.18) 0 9px, transparent 10px),
      linear-gradient(180deg, var(--blue) 0%, var(--blue-mid) 100%);
  }
  .pattern-strip--green {
    background:
      radial-gradient(circle at 30% 12%, rgba(255,255,255,.25) 0 9px, transparent 10px),
      radial-gradient(circle at 70% 38%, rgba(255,255,255,.2) 0 11px, transparent 12px),
      radial-gradient(circle at 35% 64%, rgba(255,255,255,.22) 0 10px, transparent 11px),
      radial-gradient(circle at 68% 88%, rgba(255,255,255,.2) 0 9px, transparent 10px),
      linear-gradient(180deg, var(--green) 0%, #a7d04f 100%);
  }

  .tile { position: absolute; display: flex; align-items: center; justify-content: center; text-align: center;
          font-family: var(--heading-font); font-weight: 400; color: var(--white); font-size: 46px; line-height: 0.9; letter-spacing: 2px; }
  .tile--small { font-size: 38px; letter-spacing: 1.5px; }
  .tile--orange { background: var(--orange); }
  .tile--blue { background: var(--blue); }
  .tile--green { background: var(--green); }
  .photo { position: absolute; }

  .generic__header { position: absolute; left: 296px; top: 0; right: 0; height: 79px; background: var(--orange);
                     font-family: var(--heading-font); font-weight: 400; color: var(--white); font-size: 38px; letter-spacing: 2.5px;
                     display: flex; align-items: center; padding-left: 25px; }
  .generic__body { position: absolute; left: 296px; top: 79px; right: 0; bottom: 0; background: var(--blue);
                   padding: 19px 36px 0 25px; color: var(--white); font-size: 15px; line-height: 1.32; }
</style>
</head>
<body>

<section class="email email--welcome">
  <div class="intro">
    <div class="brand"><span class="brand__dot"></span><span class="brand__name">Bloomwell<br>Early Learning</span></div>
    <h2 class="intro__title" style="top:188px;">WELCOME</h2>
    <p class="intro__text" style="top:232px;">At Bloomwell each child's needs and interests are built on in a caring and loving.</p>
  </div>
  <div class="pattern-strip pattern-strip--blue" style="left:222px;width:74px;" role="img" aria-label="White line-drawn pattern of toys, kites, clouds and trees"></div>
  <div class="tile tile--orange" style="left:296px;top:0;width:194px;height:115px;">NURTURE</div>
  <div class="photo" style="left:490px;top:0;width:215px;height:115px;background:radial-gradient(ellipse at 30% 45%,#7a5040 0%,transparent 40%),radial-gradient(ellipse at 78% 60%,#c7a08a 0%,transparent 45%),linear-gradient(135deg,#ece6df,#b89a86);" role="img" aria-label="Photo of a teacher reading a book to a group of young children"></div>
  <div class="photo" style="left:296px;top:115px;width:194px;height:126px;background:radial-gradient(ellipse at 55% 70%,#fbf8f0 0%,transparent 32%),radial-gradient(ellipse at 55% 35%,#6b4430 0%,transparent 28%),linear-gradient(135deg,#f7d54c,#f0c02c);" role="img" aria-label="Photo of a young girl painting against a yellow wall"></div>
  <div class="tile tile--blue" style="left:490px;top:115px;width:215px;height:126px;">FLOURISH</div>
  <div class="tile tile--green" style="left:296px;top:241px;width:194px;height:108px;">GROW</div>
  <div class="photo" style="left:490px;top:241px;width:215px;height:108px;background:radial-gradient(ellipse at 30% 60%,#f08a80 0%,transparent 30%),radial-gradient(ellipse at 75% 55%,#e9ddd0 0%,transparent 35%),radial-gradient(ellipse at 50% 95%,#8fb44a 0%,transparent 30%),linear-gradient(135deg,#f3eee9,#cdbfb4);" role="img" aria-label="Photo of two toddlers playing with building blocks"></div>
</section>

<section class="email email--bring">
  <div class="intro">
    <div class="brand"><span class="brand__dot"></span><span class="brand__name">Bloomwell<br>Early Learning</span></div>
    <h2 class="intro__title" style="top:188px;font-size:38px;line-height:0.82;">WHAT TO<br>BRING</h2>
    <p class="intro__text" style="top:251px;left:22px;">At Bloomwell each child's needs and interests are built on in a caring. And loving environment.</p>
  </div>
  <div class="pattern-strip pattern-strip--blue" style="left:222px;width:73px;" role="img" aria-label="White line-drawn pattern of teddy bears, pencils, stars and toys"></div>
  <div class="tile tile--green tile--small" style="left:295px;top:0;width:194px;height:120px;">LUNCH</div>
  <div class="photo" style="left:489px;top:0;width:216px;height:120px;background:radial-gradient(ellipse at 40% 50%,#c98040 0%,transparent 35%),radial-gradient(ellipse at 88% 65%,#c7df9a 0%,transparent 28%),linear-gradient(135deg,#efeae4,#dcd3c8);" role="img" aria-label="Photo of a fun lunch box with a sandwich and fruit"></div>
  <div class="photo" style="left:295px;top:120px;width:194px;height:120px;background:linear-gradient(120deg,transparent 38%,#f3c232 40%,#f3c232 43%,transparent 45%,transparent 52%,#f3c232 54%,#f3c232 57%,transparent 59%),linear-gradient(135deg,#d6b48c,#f2f0ec);" role="img" aria-label="Photo of pencils resting on notebooks"></div>
  <div class="tile tile--blue tile--small" style="left:489px;top:120px;width:216px;height:120px;">PEN &amp;<br>PAPER</div>
  <div class="tile tile--orange tile--small" style="left:295px;top:240px;width:194px;height:109px;">EXTRA<br>CLOTHING</div>
  <div class="photo" style="left:489px;top:240px;width:216px;height:109px;background:radial-gradient(ellipse at 55% 40%,#c85060 0%,transparent 25%),radial-gradient(ellipse at 50% 85%,#f0d6e0 0%,transparent 50%),linear-gradient(180deg,#f6dc6a,#f1e4e8);" role="img" aria-label="Photo of folded children's clothes with small shoes on top"></div>
</section>

<section class="email email--generic">
  <div class="intro">
    <div class="brand"><span class="brand__dot"></span><span class="brand__name">Bloomwell<br>Early Learning</span></div>
  </div>
  <div class="pattern-strip pattern-strip--green" style="left:224px;width:72px;" role="img" aria-label="White line-drawn pattern of rockets, rainbows, boats and sea creatures"></div>
  <h2 class="generic__header">GENERIC TEMPLATE</h2>
  <p class="generic__body">At Bloomwell each child's needs and interests are built on in a caring and loving environment. We have a deep appreciation of the significance of developing each child's potential, at their own pace, and our devoted team aim to provide a warm and welcoming environment, full of stimulating experiences and discoveries.</p>
</section>

</body>
</html>
```